Australian Training Organisation Needs a Flyer for Tourism Training

I am an Australian Registered Training Organisation and have flyers that I would like to have designed. We deliver training to our local market in Tourism Hospitality and Events. You can see some examples of other brochures we have designed at http://www.kelvoramesh.com.au/bus-admin-management.html I would like something that is very modern, two sided and visual. I have added information about the training - a couple of very important things to note: All the information must be on the flyer, including codes of course. The two logos must be on the flyer (the upside down triangle logo must be next to the name Cert II in Tourism. The wording, KL Drovemark Pty Ltd (RTO 48167) must be on the flyer (can be down bottom in small text). We also have a promotion - a FREE 2 day barista course for every enrolment. I have another 3 flyers in same format to do for the successful designer.

Target Market(s)

Gen Y - Z

Industry/Entity Type

Tourism

Requirements
Must have
• Both logos
• KL Drovemark Pty Ltd (RTO 48167)
• All course codes
• All the information that is on the attached brief
Nice to have
• Very visual, without being too busy
• pictures of happy students

```html
<!DOCTYPE html>
<html lang="en">
<head>
<meta charset="utf-8">
<title>SIT20112 Certificate II in Tourism</title>
<link rel="stylesheet" href="https://fonts.googleapis.com/css2?family=Roboto:wght@300;400;500&display=swap">
<style>
  :root {
    --red: #e8304b;
    --grey: #9c9c9c;
    --mint: #dcece3;
    --butter: #f2f08c;
    --ink: #4a4a4a;
    --white: #ffffff;
    --photo-a: #c9b8a4;
    --photo-b: #e6dccf;
  }
  * { margin: 0; padding: 0; box-sizing: border-box; }
  html, body { width: 848px; height: 1200px; overflow: hidden; background: var(--white); }
  .flyer {
    position: relative; width: 848px; height: 1200px; overflow: hidden;
    background: var(--grey); font-family: "Roboto", Arial, sans-serif;
  }
  .backdrop { position: absolute; inset: 0; }
  .course-title {
    position: absolute; right: 32px; top: 326px; text-align: right;
    color: var(--white); font-weight: 400; font-size: 41px; line-height: 52px; letter-spacing: 0.3px;
  }
  .unit { position: absolute; width: 365px; }
  .unit-icon {
    position: absolute; left: 0; top: -8px; width: 48px; height: 48px; border-radius: 50%;
    background: var(--white); border: 4px solid var(--red);
    display: flex; align-items: center; justify-content: center; z-index: 2;
    box-shadow: -3px 2px 0 rgba(0,0,0,0.08);
  }
  .unit-icon svg { width: 24px; height: 24px; }
  .unit.is-mint .unit-icon { border-color: var(--mint); }
  .unit.is-butter .unit-icon { border-color: var(--butter); }
  .unit-code {
    margin-left: 23px; height: 31px; padding-left: 39px; line-height: 31px;
    background: var(--red); color: var(--white); font-size: 17px; font-weight: 400;
  }
  .unit.is-mint .unit-code { background: var(--mint); color: var(--ink); }
  .unit.is-butter .unit-code { background: var(--butter); color: var(--ink); }
  .unit-name {
    margin-left: 62px; margin-top: 6px; color: var(--white);
    font-size: 15px; font-weight: 300; line-height: 19px;
  }
  .accreditation {
    position: absolute; left: 56px; top: 979px; width: 244px; height: 244px; border-radius: 50%;
    background: var(--white); border: 9px solid var(--red);
    display: flex; flex-direction: column; align-items: center; justify-content: flex-start;
    padding-top: 62px; gap: 10px;
  }
  .accreditation-mark { width: 22px; height: 22px; background: var(--red); }
  .accreditation-name {
    text-align: center; color: #1d5c3a; font-size: 15px; font-weight: 500; line-height: 19px;
  }
  .contact {
    position: absolute; right: 28px; top: 1046px; text-align: right; color: var(--white); font-weight: 300;
  }
  .contact-web { font-size: 35px; line-height: 46px; }
  .contact-phone { font-size: 41px; line-height: 48px; }
  .legal {
    position: absolute; right: 28px; top: 1176px; text-align: right;
    color: var(--ink); font-size: 11px; font-weight: 400; line-height: 14px;
  }
  .legal strong { color: var(--red); font-weight: 500; }
</style>
</head>
<body>
<main class="flyer">
  <svg class="backdrop" width="848" height="1200" viewBox="0 0 848 1200" aria-hidden="true">
    <defs>
      <linearGradient id="photo-tone" x1="0" y1="0" x2="1" y2="1">
        <stop offset="0" stop-color="var(--photo-a)"/>
        <stop offset="1" stop-color="var(--photo-b)"/>
      </linearGradient>
    </defs>
    <g role="img" aria-label="Photographs of smiling school students with backpacks">
      <rect x="0" y="0" width="848" height="320" fill="url(#photo-tone)"/>
      <rect x="300" y="0" width="3" height="300" fill="#ffffff"/>
    </g>
    <polygon points="0,180 568,292 848,240 848,438 205,438 330,372 0,372" fill="var(--red)"/>
    <polyline points="0,194 568,300 848,250" fill="none" stroke="#ffffff" stroke-width="5"/>
    <polygon points="0,372 310,372 0,408" fill="var(--mint)"/>
    <polygon points="205,438 848,438 848,478" fill="var(--butter)"/>
    <polygon points="0,966 640,990 0,990" fill="var(--butter)"/>
    <polygon points="0,990 640,990 848,1040 848,1160 0,1185" fill="var(--red)"/>
    <polygon points="600,1040 848,1025 848,1040" fill="var(--mint)"/>
    <polygon points="0,1185 848,1160 848,1200 0,1200" fill="#ffffff"/>
  </svg>

  <h1 class="course-title">SIT20112 CERTIFICATE II<br>IN TOURISM</h1>

  <div class="unit" style="left:23px; top:508px;">
    <div class="unit-icon"><svg viewBox="0 0 24 24"><path d="M6 3h3v4l2 3v11H4V10l2-3z M15 4h5l-1 6a2 2 0 0 1-3 0z M17.5 11v8 M15 20h5" fill="none" stroke="#444" stroke-width="1.6"/></svg></div>
    <div class="unit-code">SITFAB201</div>
    <div class="unit-name">Provide responsible service of alcohol</div>
  </div>
  <div class="unit is-mint" style="left:23px; top:578px;">
    <div class="unit-icon"><svg viewBox="0 0 24 24"><circle cx="12" cy="12" r="9" fill="none" stroke="#444" stroke-width="1.6"/><path d="M6 18 18 6 M8 6v5 M10 6v5 M8 11l5 6 M16 8c-2 2-2 4 0 5" fill="none" stroke="#444" stroke-width="1.6"/></svg></div>
    <div class="unit-code">SITXFSA101</div>
    <div class="unit-name">Use hygienic practices for food safety</div>
  </div>
  <div class="unit is-butter" style="left:23px; top:648px;">
    <div class="unit-icon"><svg viewBox="0 0 24 24"><path d="M3 5l6-2 6 2 6-2v16l-6 2-6-2-6 2z M9 3v16 M15 5v16" fill="none" stroke="#444" stroke-width="1.6"/></svg></div>
    <div class="unit-code">SITXCCS201</div>
    <div class="unit-name">Provide visitor information</div>
  </div>
  <div class="unit" style="left:23px; top:717px;">
    <div class="unit-icon"><svg viewBox="0 0 24 24"><path d="M6 21V5h12v16z M9 8h2 M13 8h2 M9 12h2 M13 12h2 M9 16h2 M13 16h2" fill="none" stroke="#444" stroke-width="1.8"/></svg></div>
    <div class="unit-code">BSBCMM201A</div>
    <div class="unit-name">Communicate in the workplace</div>
  </div>
  <div class="unit is-mint" style="left:23px; top:786px;">
    <div class="unit-icon"><svg viewBox="0 0 24 24"><path d="M3 9l9-5 9 5z M5 10v8 M9.5 10v8 M14.5 10v8 M19 10v8 M3 20h18" fill="none" stroke="#444" stroke-width="1.8"/></svg></div>
    <div class="unit-code">SITXCOM201</div>
    <div class="unit-name">Show social and cultural sensitivity</div>
  </div>
  <div class="unit is-butter" style="left:23px; top:857px;">
    <div class="unit-icon"><svg viewBox="0 0 24 24"><circle cx="8" cy="10" r="3" fill="none" stroke="#444" stroke-width="1.6"/><path d="M3 20c0-4 10-4 10 0 M14 4h7v5h-4l-2 2v-2h-1z" fill="none" stroke="#444" stroke-width="1.6"/></svg></div>
    <div class="unit-code">SITLAD001</div>
    <div class="unit-name">Conduct basic oral communication in a<br>language other than English</div>
  </div>

  <div class="unit" style="left:438px; top:508px;">
    <div class="unit-icon"><svg viewBox="0 0 24 24"><path d="M3 7h18v13H3z M9 7V4h6v3 M12 10v7 M8.5 13.5h7" fill="none" stroke="#444" stroke-width="1.7"/></svg></div>
    <div class="unit-code">HLTAID003</div>
    <div class="unit-name">Provide first aid</div>
  </div>
  <div class="unit is-mint" style="left:438px; top:578px;">
    <div class="unit-icon"><svg viewBox="0 0 24 24"><path d="M7 3l5 6 5-6 3 3v15H4V6z M12 9v12 M4 14h16" fill="none" stroke="#444" stroke-width="1.6"/></svg></div>
    <div class="unit-code">SITXWHS101</div>
    <div class="unit-name">Participate in safe work practices</div>
  </div>
  <div class="unit is-butter" style="left:438px; top:648px;">
    <div class="unit-icon"><svg viewBox="0 0 24 24"><path d="M4 5h16l-2 4h-5l-3 11H6l3-11H3z" fill="#444"/></svg></div>
    <div class="unit-code">SITXFIN201</div>
    <div class="unit-name">Process financial transactions</div>
  </div>
  <div class="unit" style="left:438px; top:717px;">
    <div class="unit-icon"><svg viewBox="0 0 24 24"><circle cx="12" cy="6" r="3" fill="#444"/><circle cx="5" cy="15" r="2.5" fill="#444"/><circle cx="19" cy="15" r="2.5" fill="#444"/><path d="M12 9v5 M5 18v3 M19 18v3 M8 21h8v-5H8z" fill="#444" stroke="#444" stroke-width="1.4"/></svg></div>
    <div class="unit-code">SITXCC202</div>
    <div class="unit-name">Interact with customers</div>
  </div>
  <div class="unit is-mint" style="left:438px; top:786px;">
    <div class="unit-icon"><svg viewBox="0 0 24 24"><path d="M3 6h7l2 2h9v12H3z M3 10h18" fill="none" stroke="#444" stroke-width="1.7"/></svg></div>
    <div class="unit-code">STITIND201</div>
    <div class="unit-name">Source and use information on the tourism<br>and travel industry</div>
  </div>

  <div class="accreditation">
    <span class="accreditation-mark"></span>
    <span class="accreditation-name">Registered Skills<br>Training</span>
  </div>

  <div class="contact">
    <p class="contact-web">www.kelvoramesh.com.au</p>
    <p class="contact-phone">07 40552913</p>
  </div>

  <p class="legal"><strong>FREE 2 day barista course with every enrolment</strong> · KL Drovemark Pty Ltd (RTO 48167)</p>
</main>
</body>
</html>
```